Minimalist Professional Business Card Design

We will be revamping our marketing materials: Business cards, Website and Catalogs.
Our Overall Design direction is to have a Minimalist artwork with Professionalism and Premium feel. The revamp starts with the new business card design followed by the others. Thus the designer whom work is selected for this job will likely to follow through with the subsequent jobs.

Target Market(s)

Upscale

Industry/Entity Type

Manufacturing

Contact Information for Business Card

For the Business Cards, the following are required:
. Minimalist yet Professional and Premium Feel
. Background Colors: white and / or light pastel yellow and if needed to smoothen the yellow, the light grey can be incorporated. We are changing our corporate bright yellow to either one of the three alternatives:
1. Soylant yellow CMYK (1%, 0%, 52%, 3%)
2. Popcorn yellow CMYK (0%, 0%, 33%, 0%)
3. Papaya yellow CMYK (0%, 0%, 51%, 0%)

Information to be inputed in the business cards:

Name: Ravel Amwerdi
Position: Managing Director

Company's name: Brolvane Valves Pte. Ltd.
Address: 412 Telbrook Lane #07-09K
Singapore 731852
Tel: (65) 6281 9046
Fax: (65) 6287 1149
Email: ravel@brolvanevalves.example
Website: www.brolvanevalves.example
Skype: Brolvane.Valves
Whatsapp/ Line/ Viber/ WeChat: (65) 9827 6013

Company's Logo
Company's Slogan
Two product photos placed side by side (if this gets into the way of the design, it is OK not to include them)

Font styles to use
Serif

Colors
ffffff

Requirements
Must have
• Minimalist
Should not have
• Messy, crowded, playful

```html
<!DOCTYPE html>
<html lang="en">
<head>
<meta charset="utf-8">
<title>Brolvane Valves – Business Card</title>
<link rel="stylesheet" href="https://fonts.googleapis.com/css2?family=PT+Sans:wght@400;700&family=PT+Sans+Narrow:wght@700&display=swap">
<style>
  :root {
    --backdrop: #2b2b2b;
    --card-white: #f4f4f4;
    --band-grey: #5d5d5d;
    --ink: #5a5a5a;
    --ink-dark: #4a4a4a;
    --rule: #9a9a9a;
    --on-dark: #ffffff;
    --product-light: #d8d8d8;
    --product-mid: #9c9c9c;
  }
  html, body {
    margin: 0;
    width: 1200px;
    height: 960px;
    overflow: hidden;
    background: var(--backdrop);
  }
  .canvas { position: relative; width: 1200px; height: 960px; }
  .card {
    position: absolute;
    width: 598px;
    height: 342px;
    border-radius: 18px;
    overflow: hidden;
    font-family: "PT Sans", sans-serif;
  }
  .card-front { left: 322px; top: 110px; background: var(--card-white); }
  .card-back { left: 320px; top: 493px; background: var(--band-grey); }
  .front-bands { position: absolute; inset: 0; }
  .brand-block {
    position: absolute;
    left: 40px; top: 78px; width: 232px;
    text-align: center;
  }
  .brand-ring {
    width: 112px; height: 112px;
    margin: 0 auto;
    border: 14px solid var(--ink);
    border-radius: 50%;
    box-sizing: border-box;
  }
  .brand-name {
    margin-top: 14px;
    font-family: "PT Sans Narrow", sans-serif;
    font-weight: 700;
    font-size: 58px;
    line-height: 1;
    letter-spacing: 1px;
    color: var(--ink);
  }
  .divider {
    position: absolute;
    left: 288px; top: 75px;
    width: 1px; height: 220px;
    background: var(--rule);
  }
  .contact {
    position: absolute;
    left: 320px; top: 74px;
    color: var(--ink);
  }
  .person-name { margin: 0; font-size: 20px; font-weight: 700; line-height: 22px; color: var(--ink-dark); }
  .person-role { margin: 0 0 12px; font-size: 15px; font-weight: 700; line-height: 18px; color: #333; }
  .address { margin: 0 0 4px; font-size: 14.5px; line-height: 19.5px; }
  .contact-list { list-style: none; margin: 0; padding: 0; font-size: 14.5px; line-height: 19.6px; }
  .contact-list li { display: flex; align-items: center; gap: 8px; }
  .contact-list svg { width: 13px; height: 13px; flex: none; fill: var(--ink); }
  .product-photos {
    position: absolute;
    left: 225px; top: 50px;
    width: 148px; height: 228px;
    border-radius: 6px;
    background: linear-gradient(90deg, var(--product-mid), var(--product-light) 30%, var(--product-mid) 48%, var(--band-grey) 50%, var(--product-mid) 56%, var(--product-light) 75%, var(--product-mid));
  }
  .slogan {
    position: absolute;
    left: 0; right: 0; top: 294px;
    margin: 0;
    text-align: center;
    font-family: "PT Sans Narrow", sans-serif;
    font-weight: 700;
    font-size: 19px;
    color: var(--on-dark);
  }
</style>
</head>
<body>
<main class="canvas">
  <section class="card card-front">
    <svg class="front-bands" viewBox="0 0 598 342" aria-hidden="true">
      <path d="M0 0 H598 V2 C420 2 180 20 0 62 Z" fill="#5d5d5d"/>
      <path d="M598 278 C520 310 300 335 0 342 H598 Z" fill="#5d5d5d"/>
    </svg>
    <div class="brand-block">
      <div class="brand-ring"></div>
      <div class="brand-name">BROLVANE</div>
    </div>
    <div class="divider"></div>
    <div class="contact">
      <p class="person-name">RAVEL AMWERDI</p>
      <p class="person-role">MANAGING DIRECTOR</p>
      <p class="address">Brolvane Valves Pte. Ltd.<br>412 Telbrook Lane #07-09K<br>Singapore 731852</p>
      <ul class="contact-list">
        <li><svg viewBox="0 0 16 16"><path d="M1 6 C1 3 15 3 15 6 V8 H11 V6 H5 V8 H1 Z M3 9 H13 L14 14 H2 Z"/></svg>(65) 6281 9046</li>
        <li><svg viewBox="0 0 16 16"><path d="M4 1 H12 V5 H4 Z M1 6 H15 V12 H12 V15 H4 V12 H1 Z"/></svg>(65) 6287 1149</li>
        <li><svg viewBox="0 0 16 16"><circle cx="8" cy="8" r="7"/></svg>(65) 9827 6013</li>
        <li><svg viewBox="0 0 16 16"><path d="M1 3 H15 V13 H1 Z" /><path d="M1 3 L8 9 L15 3" fill="none" stroke="#f4f4f4" stroke-width="1.5"/></svg>ravel@brolvanevalves.example</li>
        <li><svg viewBox="0 0 16 16"><circle cx="8" cy="8" r="7"/><path d="M1 8 H15 M8 1 C4 5 4 11 8 15 M8 1 C12 5 12 11 8 15" fill="none" stroke="#f4f4f4" stroke-width="1.2"/></svg>www.brolvanevalves.example</li>
        <li><svg viewBox="0 0 16 16"><circle cx="8" cy="8" r="7"/></svg>Brolvane.Valves</li>
      </ul>
    </div>
  </section>

  <section class="card card-back">
    <div class="product-photos" role="img" aria-label="Two stainless steel submersible pump products standing side by side"></div>
    <p class="slogan">Made With Pride I For Heavy Duty</p>
  </section>
</main>
</body>
</html>
```